Come crowdsource a Web Design for a brazilian crowdsource Startup!

> NAME OF OUR STARTUP:
Vantremo

> DESCRIPTION OF OUR STARTUP:
We are a crowdsourcing startup in Brazil providing consultancy and technology to support other companies to crowdsource their projects.
We also operate doing big crowdsource campaings related to polemic subjects in Brazil.

> WHAT ARE OUR TARGET AUDIENCE?
Our target audience are young people around 20-35 years old.
Generation Y (Millennial Generation)

> WHAT IS OUR INDUSTRY?
Internet, web

> WHAT DO WE NEED?
We need a Web Design for our first site.

We need 5 pages:
- Home
- What is Crowdsourcing?
- Solutions
- About Us
- Blog
- A box for the "Contact" tab (this is not a page)

Please, find attached a Layout Sketch of what I've imagined.

Lets talk about the sketch:
Well, first of all, it's a SKETCH, so you don't have to send proposals exactly as the sketch. The sketch is just to show how I've imagined the ditribution of the content boxes. For example, the menu bar doesnt need to be a rectangle exactly like the sketch, but, I would like to have the menu on the right side of the logo. Also, you will see that the boxes are all squeezed, of course I dont want them soo squeezed! Again, its juust a SKETCH!

About the images on the sketch:
IMG1 - Some nice and simple image related to collectivity or related to crowdsourcing or maybe use our O logo.

IMG2 - Some simple and creative image related to Consultancy. It doesnt need to be so obvious.

IMG3 - Some simple and creative image related to Web 2.0 Software Technology. It doesnt need to be so obvious.

IMG4 - Some simple and creative image related to a full package of Consultancy + Technology. It doesnt need to be so obvious.

IMG5 - Some nice and simple image related to collectivity or related to crowdsourcing.

IMG6 - Some nice and simple image related to Ideation. Maybe a light bulb? I dont know, be creative!

IMG7 - Some nice and simple image related to Crowdlabor. I dont know, be creative!

IMG8 - Some nice and simple image related to CrowdFeedback. Maybe a megaphone? A loudspeaker? I dont know, be creative!

IMG9 - Some nice and simple image related to us! Maybe our O logo ? I dont know, be creative!

THE CONTACT SIDE BAR - we need a nice and simple contact side bar. By the way, on the sketch this bar is shown only at the homepage, but when the site becomes real this bar will stay along all the pages.

THE CONTACT BOX - we need a nice and simple contact box.

ABOUT THE COLORS TO USE: we would like some color to our background and titles. We like colors similars to our logo: really light blue ? light green/blue ? light grey ? light orange ? I dont know, you guys knows more about that then me =)

PLIMBOOK SHARE/LIKE BUTTON: We would like a plimbook share/like button somewhere on the site!

ABOUT THE ATTACHED FILES:

ADDITIONALS:
> The name Vantremo comes from "collectivity". With our name we want to pass the idea of the collectivity from the crowdsource work model.

> Our communication is directed to the Generation Y.

> Remember, we are a Startup! So we need a modern and simple site, something like the web 2.0 trends. It must be beautiful =)

> We arent a serious company. We are a young and fun company! Please, dont come with old fashionable company sites.

> Be creative =] !

Target Market(s)

Our target audience are young people around 20-35 years old. Generation Y (Millennial Generation)

Industry/Entity Type

Communication

Requirements
Must have
• We need a Web Design for our first site.

We need 5 pages:
- Home
- What is Crowdsourcing?
- Solutions
- About Us
- Blog

ABOUT THE COLORS TO USE: we would like some color to our background and titles. We like colors similars to our logo: really light blue ? light green/blue ? light grey ? light oranges ? I dont know, you guys knows more about that then me =)

Should not have
• Poor/serious/old fashionable designs

```html
<!DOCTYPE html>
<html lang="en">
<head>
<meta charset="utf-8">
<title>Vantremo — Solutions</title>
<link href="https://fonts.googleapis.com/css2?family=PT+Sans:ital,wght@0,400;0,700;1,700&family=Baloo+2:wght@700&display=swap" rel="stylesheet">
<style>
  :root {
    --teal: #127f8c;
    --teal-dark: #0d6a75;
    --sky-light: #c6e8ef;
    --sky: #92d1dc;
    --paper: #ffffff;
    --ink: #111111;
    --body-text: #3a3a3a;
    --lead-text: #0f7d86;
    --accent-orange: #f0a030;
    --cta-yellow: #f3c100;
    --contact-red: #e3262b;
    --hole: #bfe6ee;
    --footer: #333333;
  }
  * { box-sizing: border-box; margin: 0; padding: 0; }
  html, body { width: 1113px; height: 1200px; overflow: hidden; }
  body {
    position: relative;
    font-family: "PT Sans", sans-serif;
    background: linear-gradient(to bottom, var(--sky-light) 0, var(--sky-light) 666px, var(--sky) 666px, var(--sky) 100%);
  }
  .site-header {
    position: absolute; left: 0; top: 0; width: 1113px; height: 122px;
    background: var(--teal);
    border-bottom: 2px solid var(--teal-dark);
  }
  .brand {
    position: absolute; left: 40px; top: 26px;
    display: flex; align-items: center; gap: 12px;
    font-family: "Baloo 2", sans-serif; font-weight: 700;
    font-size: 62px; line-height: 1; color: #ffffff;
  }
  .brand-dot { width: 44px; height: 44px; border-radius: 50%; background: #ffffff; }
  .main-nav {
    position: absolute; right: 42px; top: 44px;
    display: flex; gap: 36px;
    font-size: 23px; color: #ffffff;
  }
  .main-nav a { color: inherit; text-decoration: none; }
  .main-nav .is-current { color: var(--accent-orange); }

  .page-sheet {
    position: absolute; left: 44px; top: 153px; width: 1026px; height: 963px;
    background: var(--paper);
    box-shadow: 4px 6px 8px rgba(0,0,0,0.25);
  }
  .binder-holes { position: absolute; left: 0; top: 0; }

  .solution {
    position: absolute; top: 0; width: 284px; text-align: center;
  }
  .solution-art {
    width: 212px; height: 212px; margin: 93px auto 0;
    border-radius: 50%;
    border: 9px solid var(--accent-orange);
    background: radial-gradient(circle at 50% 40%, #dfeeee 0, #a9c9c8 70%);
  }
  .solution-title {
    margin-top: 40px;
    font-size: 24px; font-weight: 400; color: var(--ink);
  }
  .solution-copy {
    margin-top: 14px; text-align: justify;
    font-size: 12px; line-height: 15.8px; color: var(--body-text);
  }
  .solution-copy p + p { margin-top: 16px; }
  .solution-copy .lead { color: var(--lead-text); }
  .solution-cta {
    margin-top: 42px;
    font-size: 12.5px; line-height: 16px; font-style: italic; font-weight: 700;
    color: var(--cta-yellow);
  }

  .share-tab {
    position: absolute; left: 1066px; top: 340px; width: 47px; height: 66px;
    background: var(--teal); color: #ffffff; text-align: center;
    font-size: 14px; font-weight: 700; padding-top: 6px;
  }
  .share-tab .share-dot {
    width: 22px; height: 22px; border-radius: 50%; background: #4ea9b3;
    margin: 8px auto 0;
  }
  .contact-tab {
    position: absolute; left: 1066px; top: 413px; width: 47px; height: 142px;
    background: var(--contact-red);
    border: 3px solid #ffffff; border-right: none;
    box-shadow: 0 0 0 2px var(--contact-red);
  }
  .contact-tab span {
    position: absolute; left: 50%; top: 50%;
    transform: translate(-50%, -50%) rotate(-90deg);
    white-space: nowrap; font-size: 20px; color: #ffffff;
  }

  .site-footer {
    position: absolute; left: 0; top: 1152px; width: 1113px; height: 48px;
    background: var(--footer); color: #ffffff;
    font-size: 12.5px; text-align: center; line-height: 48px;
  }
</style>
</head>
<body>
  <header class="site-header">
    <div class="brand"><span class="brand-dot"></span>Vantremo</div>
    <nav class="main-nav">
      <a href="#">What Is Crowdsourcing</a>
      <a href="#" class="is-current">Solutions</a>
      <a href="#">About Us</a>
      <a href="#">Blog</a>
    </nav>
  </header>

  <main class="page-sheet">
    <svg class="binder-holes" width="1026" height="40" aria-hidden="true">
      <g fill="var(--hole)">
        <circle cx="23" cy="21" r="13.5"/><circle cx="88.5" cy="21" r="13.5"/>
        <circle cx="154" cy="21" r="13.5"/><circle cx="219.5" cy="21" r="13.5"/>
        <circle cx="285" cy="21" r="13.5"/><circle cx="350.5" cy="21" r="13.5"/>
        <circle cx="416" cy="21" r="13.5"/><circle cx="481.5" cy="21" r="13.5"/>
        <circle cx="547" cy="21" r="13.5"/><circle cx="612.5" cy="21" r="13.5"/>
        <circle cx="678" cy="21" r="13.5"/><circle cx="743.5" cy="21" r="13.5"/>
        <circle cx="809" cy="21" r="13.5"/><circle cx="874.5" cy="21" r="13.5"/>
        <circle cx="940" cy="21" r="13.5"/><circle cx="1005.5" cy="21" r="13.5"/>
      </g>
    </svg>

    <section class="solution" style="left:43px">
      <div class="solution-art" role="img" aria-label="Illustration of a consultant in a suit beside a speech bubble full of colourful dots"></div>
      <h2 class="solution-title">Consultancy</h2>
      <div class="solution-copy">
        <p class="lead">Crowdsourcing is the process of getting work or funding, usually online, from a crowd of people. The word is a combination of the words 'crowd' and 'outsourcing'. The idea is to take work and outsource it to a crowd of workers.</p>
        <p>Crowdsourcing’s biggest benefit is the ability to receive better quality results, since several people offer their best ideas, skills, &amp; support. Crowdsourcing allows you to select the best result from a sea of ‘best entries,’ as opposed to receiving the best entry from a single provider. Results can be delivered much quicker than traditional methods, since crowdsourcing is a form of freelancing. You can get a finished video within a month, a finished design or idea within a week, and microtasks appear within minutes.</p>
        <p>Clear instructions are essential in crowdsourcing. You could potentially be searching through thousands of possible ideas, which can be painstaking, or even complicated, if the instructions are not clearly understood. Some forms of crowdsourcing do involve spec work, which some people are against. Quality can be difficult to judge if proper expectations are not clearly stated.</p>
      </div>
      <p class="solution-cta">Get in touch with us right now<br>for questions and prices.</p>
    </section>

    <section class="solution" style="left:370px">
      <div class="solution-art" role="img" aria-label="Illustration of a desktop monitor, tablet and smartphone"></div>
      <h2 class="solution-title">Technology</h2>
      <div class="solution-copy">
        <p class="lead">Crowdsourcing is the process of getting work or funding, usually online, from a crowd of people. The word is a combination of the words 'crowd' and 'outsourcing'. The idea is to take work and outsource it to a crowd of workers.</p>
        <p>Crowdsourcing’s biggest benefit is the ability to receive better quality results, since several people offer their best ideas, skills, &amp; support. Crowdsourcing allows you to select the best result from a sea of ‘best entries,’ as opposed to receiving the best entry from a single provider. Results can be delivered much quicker than traditional methods, since crowdsourcing is a form of freelancing. You can get a finished video within a month, a finished design or idea within a week, and microtasks appear within minutes.</p>
        <p>Clear instructions are essential in crowdsourcing. You could potentially be searching through thousands of possible ideas, which can be painstaking, or even complicated, if the instructions are not clearly understood. Some forms of crowdsourcing do involve spec work, which some people are against. Quality can be difficult to judge if proper expectations are not clearly stated.</p>
      </div>
      <p class="solution-cta">Get in touch with us right now<br>for questions and prices.</p>
    </section>

    <section class="solution" style="left:699px">
      <div class="solution-art" role="img" aria-label="Illustration of a consultant holding a tablet and phone showing colourful dots"></div>
      <h2 class="solution-title">Consultancy + Technology</h2>
      <div class="solution-copy">
        <p class="lead">Crowdsourcing is the process of getting work or funding, usually online, from a crowd of people. The word is a combination of the words 'crowd' and 'outsourcing'. The idea is to take work and outsource it to a crowd of workers.</p>
        <p>Crowdsourcing’s biggest benefit is the ability to receive better quality results, since several people offer their best ideas, skills, &amp; support. Crowdsourcing allows you to select the best result from a sea of ‘best entries,’ as opposed to receiving the best entry from a single provider. Results can be delivered much quicker than traditional methods, since crowdsourcing is a form of freelancing. You can get a finished video within a month, a finished design or idea within a week, and microtasks appear within minutes.</p>
        <p>Clear instructions are essential in crowdsourcing. You could potentially be searching through thousands of possible ideas, which can be painstaking, or even complicated, if the instructions are not clearly understood. Some forms of crowdsourcing do involve spec work, which some people are against. Quality can be difficult to judge if proper expectations are not clearly stated.</p>
      </div>
      <p class="solution-cta">Get in touch with us right now<br>for questions and prices.</p>
    </section>
  </main>

  <aside class="share-tab">share<div class="share-dot"></div></aside>
  <aside class="contact-tab"><span>Contact Us</span></aside>

  <footer class="site-footer">Copyright 2013 Vantremo. All Rights Reserved.</footer>
</body>
</html>
```